Pine Hollow Lodge Retreat CD Package Design Project

This is a fund-raising CD for A WKRT family camp. The look and feel should be outdoors, campy, woodsy, wholesome, and family in feel. The camp has approximately 60 families each week staying in cabins, eating in the dining hall and doing lots of different activities. There are 11 weeks of family camping with year round weekend activities for families.
The package consists of a CD package with 4 panels plus the CD itself. The panels are Cover, Inside left, inside right and back cover. Details, and direction for each panel is below. The templates are included as well. If you use a background texture or color for the panels, it CANNOT be red or green. These two colors were used for the previous two CDs.
Updates
I posted two additional files which show the design of the previous CD. Â This is for reference only. Â The format is different. Â
Requirements
Must have
- The cover must include the "New Cabin" photo. There are 5 word docs with the required text and suggestions for content for each of the panels. There are additional photos to use if it makes sense.
Fonts should match the feel of the CD.
The front cover should have a burst indicated on the instructions for front cover.
Nice to have
- I would like one of the photos to be used for the inside right panel and that same photo used and scaled back for the CD. This isn't a must have, but a suggestion.
The previous two CDs had a background texture/color that ran through the entire package. The previous colors used were Red and Green. This is not a requirement, but if it makes sense to do this, please do not use these colors.
Should not have
- The feel should be wholesome and not contain any materials that would be viewed as offensive or sexual in nature.

```html
<!DOCTYPE html>
<html lang="en">
<head>
<meta charset="utf-8">
<title>There's a Porch on Every Cabin – CD Package</title>
<link rel="stylesheet" href="https://fonts.googleapis.com/css2?family=Kalam:wght@400;700&display=swap">
<style>
  :root{
    --page:#ffffff;
    --wood-light:#b9b2a6;
    --wood-mid:#8f8577;
    --wood-dark:#4d3f33;
    --paper:#f4eccb;
    --paper-edge:#c9a65a;
    --paper-burn:#6b4a1f;
    --rule:#9fc3c9;
    --ink:#1d1a16;
    --forest-light:#7fd13a;
    --forest-dark:#2f5a1c;
    --cabin:#d97b5c;
    --frame:#ffffff;
  }
  *{box-sizing:border-box;margin:0;padding:0}
  html,body{width:1200px;height:1000px;overflow:hidden;background:var(--page)}
  body{font-family:"Kalam",cursive;color:var(--ink);position:relative}

  .wood{position:absolute;left:75px;top:35px;width:1065px;height:940px;
    background:
      repeating-linear-gradient(90deg,rgba(0,0,0,.06) 0 2px,transparent 2px 14px),
      linear-gradient(180deg,var(--wood-light) 0%,var(--wood-mid) 45%,var(--wood-dark) 78%,var(--wood-mid) 100%);}
  .fold{position:absolute;background:rgba(0,0,0,.25)}
  .fold.v{left:605px;top:35px;width:2px;height:940px}
  .fold.h{left:75px;top:505px;width:1065px;height:2px}

  .disc{position:absolute;left:118px;top:53px;width:444px;height:444px;border-radius:50%;
    background:radial-gradient(circle at 50% 55%,var(--forest-light) 0%,#5aa82c 45%,var(--forest-dark) 100%);
    box-shadow:0 2px 6px rgba(0,0,0,.35)}
  .disc-hole{position:absolute;left:170px;top:170px;width:104px;height:104px;border-radius:50%;
    background:linear-gradient(180deg,var(--wood-light),var(--wood-mid));box-shadow:inset 0 0 4px rgba(0,0,0,.5)}

  .paper{position:absolute;border-radius:14px;
    background:
      repeating-linear-gradient(180deg,transparent 0 16px,var(--rule) 16px 17px),
      radial-gradient(ellipse at center,var(--paper) 60%,var(--paper-edge) 92%,var(--paper-burn) 100%);}

  .credits{left:645px;top:40px;width:466px;height:452px;transform:rotate(180deg);
    padding:14px 22px 10px;font-size:11.2px;line-height:17px}
  .credits h3{font-size:15px;font-weight:700}
  .credits b{font-weight:700}
  .credits .indent{padding-left:150px}

  .tracklist{left:170px;top:515px;width:372px;height:442px;padding:24px 20px 10px;text-align:center;font-size:13px;line-height:17px}
  .tracklist h2{font-size:16px;font-weight:400}
  .tracklist ol{list-style:none;text-align:left;margin:14px 0 0 56px;font-size:14px;line-height:15.5px}
  .brand{display:flex;align-items:center;justify-content:center;gap:8px;margin-top:26px;font-size:14px;letter-spacing:2px}
  .brand i{width:12px;height:12px;border-radius:50%;background:var(--ink);display:block}
  .tracklist .buy{position:absolute;left:0;right:0;bottom:10px;font-size:12.5px;line-height:16px}

  .cover{left:682px;top:515px;width:390px;height:442px;padding:22px 10px 0;text-align:center}
  .cover h1{font-size:20px;font-weight:700;line-height:22px}
  .cover .sub{font-size:15px;line-height:17px}
  .cover .featuring{position:absolute;left:12px;bottom:16px;font-size:13px}

  .photo-frame{position:absolute;left:640px;top:597px;width:467px;height:310px;background:var(--frame);padding:9px;box-shadow:0 2px 6px rgba(0,0,0,.4)}
  .cabin-photo{width:100%;height:100%;
    background:linear-gradient(180deg,#4e7a2e 0%,#6a9c3c 40%,var(--cabin) 40%,var(--cabin) 78%,#5d8d35 78%,#3f6b25 100%)}
  .burst{position:absolute;left:842px;top:822px;width:272px;transform:rotate(-16deg);
    color:#fff;font-size:16px;line-height:17px;text-align:center;text-shadow:1px 1px 2px #000}
</style>
</head>
<body>
  <div class="wood" role="img" aria-label="Weathered wood plank texture background"></div>
  <div class="fold v"></div>
  <div class="fold h"></div>

  <div class="disc" role="img" aria-label="CD face: forest path through green trees">
    <div class="disc-hole"></div>
  </div>

  <section class="paper credits">
    <h3>Ben Harlow and Friends:</h3>
    <p><b>Ben Harlow</b> Guitar, Vocals, Harmonica, Buying Headphones</p>
    <p><b>Ellen Harlow</b> Vocals on "It Got Chilly Friend", Flute on "Craft Day with Ruth", Percussion on "Out by the Lake"</p>
    <p><b>Jenna Corliss</b> Vocals on "It Got Chilly Friend", "This is Pine Hollow", Percussion on "Out by the Lake"</p>
    <p><b>Owen Tasker</b> Guitar/Vocals on "Craft Day with Ruth", Vocals on "Mr. Walt Pemberton", "Peaceful PH Evening", "This is Pine Hollow"</p>
    <p><b>Molly Dunne</b> Vocals on "Peaceful PH Evening", "This is Pine Hollow"</p>
    <p><b>Hazel Quint</b> Vocals on "I Hope You Hike", "Happy Hikers", "Tough to Say Goodbye", "Out by the Lake"</p>
    <p><b>Gus Quint</b> Keyboards, Organ, Oboe, Bells, Moral support</p>
    <p><b>Walt Pemberton &amp; Carl Vossen</b> Vocals on "If They Had 10M Acorns"</p>
    <p><b>Nora Pemberton</b> Viola on "If They Had 10M Acorns"</p>
    <p><b>Sam Ridley</b> Bass</p>
    <p><b>Leo Brandt</b> Drums</p>
    <p><b>Milo Harwick</b> Guitar on "There's a Porch on Every Cabin", "I Hope You Hike", "Wish He'd Row Me Across"</p>
    <p><b>Pete Laney</b> Guitar on "Wish He'd Row Me Across"</p>
    <p><b>Special Thanks to: Walt and Nora Pemberton</b></p>
    <p class="indent">Week 6 and Labor Day family campers</p>
    <p>Artwork by</p>
    <p>Produced in conjunction with Fieldstone Records</p>
  </section>

  <section class="paper tracklist">
    <h2>There's a Porch on Every Cabin</h2>
    <p>(and other Pine Hollow improvements)</p>
    <p>Yet More Songs from Campfire by Ben Harlow and Friends</p>
    <ol>
      <li>1. There's a Porch on Every Cabin</li>
      <li>2. Mr. Walt Pemberton</li>
      <li>3. If They Had Ten Million Acorns (Live)</li>
      <li>4. Like a Tumbling Pinecone</li>
      <li>5. I Hope You Hike</li>
      <li>6. This is Pine Hollow</li>
      <li>7. It Got Chilly Friend</li>
      <li>8. Happy Hikers</li>
      <li>9. Peaceful PH Evening</li>
      <li>10. Out by the Lake</li>
      <li>11. Tough to Say Goodbye</li>
      <li>12. Last Campfire</li>
      <li>13. Craft Day with Ruth</li>
      <li>14. Wish He'd Row Me Across</li>
    </ol>
    <div class="brand"><i></i><span>PINE HOLLOW LODGE RETREAT</span></div>
    <p class="buy">To purchase this CD, call Pine Hollow at 1-800-WKRT-FUN<br>Proceeds go to the Pine Hollow Camp Improvement Fund</p>
  </section>

  <section class="paper cover">
    <h1>There's a Porch on Every Cabin</h1>
    <p class="sub">(and other Pine Hollow Improvements)</p>
    <p class="featuring">Featuring "Mr. Walt Pemberton"</p>
  </section>

  <div class="photo-frame">
    <div class="cabin-photo" role="img" aria-label="Photo of the new orange-red cabin among trees on green lawn"></div>
  </div>
  <p class="burst">Yet More Songs from Campfire by<br>Ben Harlow and Friends</p>
</body>
</html>
```